Dog care service needs business card design

Our company is Paws Harbour. We provide care for dogs while their owners are away, either through home visits or a holiday stay in the homes of carefully selected minders. Our existing website & Chatterbook cover should provide all the colour cues for our business cards - namely blues, blondes and grey. We have an existing logo (provided).

www.pawsharbourcare.example.au
www.facebook.com/pawsharbourcareau

We wish to clearly communicate our three areas of service "dog minding, home visits, dog walking".

We would like to have the files ready for upload to Printlyne (or similar) for immediate printing.

Target Market(s)

Dog owners who love their dogs like family

Industry/Entity Type

Business

Contact Information for Business Card

Paws Harbour
Ph: 0417 358 904

Font styles to use
Sans Serif

Colors
33a6d7
3176b5

Requirements
Must have
• Logo
• Telephone number
• website
• "Dog minding, home visits, dog walking"
Should not have
• any additional illustrations beyond the logo.

```html
<!DOCTYPE html>
<html lang="en">
<head>
<meta charset="utf-8">
<title>Paws Harbour – Business Card</title>
<link href="https://fonts.googleapis.com/css2?family=Lato:wght@400;700;900&display=swap" rel="stylesheet">
<style>
  :root {
    --blue-deep: #3176b5;
    --blue-bright: #33a6d7;
    --navy: #2b3a4e;
    --white: #ffffff;
    --stage: #e6e8eb;
    --photo-grass: linear-gradient(160deg, #9cc46a 0%, #5f8f3a 100%);
    --photo-door: linear-gradient(160deg, #d9cbb4 0%, #a08463 100%);
    --photo-park: linear-gradient(160deg, #7ea35a 0%, #4d7a34 100%);
  }
  * { box-sizing: border-box; margin: 0; padding: 0; }
  html, body {
    width: 1200px; height: 572px; overflow: hidden;
    background: var(--stage);
    font-family: "Lato", sans-serif;
  }
  .stage {
    width: 1200px; height: 572px;
    display: flex; align-items: center; justify-content: center;
  }
  .business-card {
    position: relative;
    width: 880px; height: 500px;
    background: var(--white);
    display: flex;
    box-shadow: 0 6px 24px rgba(0,0,0,0.18);
  }
  .card-front {
    position: relative;
    flex: 1;
  }
  .brand {
    position: absolute; left: 56px; top: 70px;
    display: flex; align-items: center; gap: 20px;
  }
  .brand-dot {
    width: 74px; height: 74px; border-radius: 50%;
    background: var(--navy);
  }
  .brand-name {
    font-weight: 900; font-size: 50px; line-height: 1;
    color: var(--navy);
  }
  .name-bar {
    position: absolute; left: 0; top: 206px;
    background: var(--blue-deep);
    color: var(--white);
    padding: 10px 24px 8px 38px;
    text-align: center;
  }
  .person-name { font-weight: 900; font-size: 31px; line-height: 1.05; letter-spacing: 0.5px; }
  .person-role { font-weight: 700; font-size: 19px; line-height: 1.1; }
  .contact-list {
    position: absolute; left: 38px; top: 300px;
    list-style: none;
    display: flex; flex-direction: column; gap: 14px;
  }
  .contact-item {
    display: flex; align-items: center; gap: 28px;
    font-weight: 700; font-size: 20px; color: var(--navy);
  }
  .contact-icon {
    width: 42px; height: 42px; border-radius: 50%;
    background: var(--blue-bright);
    display: flex; align-items: center; justify-content: center;
    flex-shrink: 0;
  }
  .services-panel {
    width: 280px; height: 100%;
    background: var(--blue-deep);
    display: flex;
    padding: 22px 0 10px 14px;
  }
  .service-list {
    list-style: none;
    display: flex; flex-direction: column; gap: 6px;
    width: 200px;
  }
  .service {
    display: flex; flex-direction: column; align-items: center;
  }
  .service-photo {
    width: 196px; height: 118px;
    border: 3px solid var(--white);
  }
  .service-photo.minding { background: var(--photo-grass); }
  .service-photo.visits { background: var(--photo-door); }
  .service-photo.walking { background: var(--photo-park); }
  .service-caption {
    color: var(--white); font-size: 17px; font-weight: 400;
    margin-top: 3px; text-transform: uppercase; letter-spacing: 0.3px;
  }
  .services-heading {
    flex: 1;
    display: flex; flex-direction: column; align-items: center; justify-content: space-between;
    padding: 10px 0 20px;
    color: var(--white); font-weight: 700; font-size: 15px;
  }
  .services-heading span {
    writing-mode: vertical-rl; text-orientation: upright;
    letter-spacing: 4px;
  }
</style>
</head>
<body>
<main class="stage">
  <article class="business-card">
    <section class="card-front">
      <div class="brand">
        <span class="brand-dot"></span>
        <span class="brand-name">Paws Harbour</span>
      </div>
      <div class="name-bar">
        <p class="person-name">TOBI ADERIN</p>
        <p class="person-role">GROUP MD/CEO</p>
      </div>
      <ul class="contact-list">
        <li class="contact-item">
          <span class="contact-icon">
            <svg width="18" height="24" viewBox="0 0 18 24"><rect x="2" y="1" width="14" height="22" rx="3" fill="none" stroke="#fff" stroke-width="2"/><circle cx="9" cy="19" r="1.4" fill="#fff"/></svg>
          </span>
          0417 358 904
        </li>
        <li class="contact-item">
          <span class="contact-icon"></span>
          pawsharbourcareau
        </li>
        <li class="contact-item">
          <span class="contact-icon">
            <svg width="24" height="24" viewBox="0 0 24 24" fill="none" stroke="#fff" stroke-width="2.2" stroke-linecap="round"><path d="M10 14l4-4"/><path d="M8.5 11.5l-2 2a3 3 0 0 0 4.2 4.2l2-2"/><path d="M15.5 12.5l2-2a3 3 0 0 0-4.2-4.2l-2 2"/></svg>
          </span>
          www.pawsharbourcare.example.au
        </li>
      </ul>
    </section>
    <aside class="services-panel">
      <ul class="service-list">
        <li class="service">
          <div class="service-photo minding" role="img" aria-label="Photo of a dog resting on green grass"></div>
          <span class="service-caption">Dog Minding,</span>
        </li>
        <li class="service">
          <div class="service-photo visits" role="img" aria-label="Photo of a dog sitting on a home doormat"></div>
          <span class="service-caption">Home Visits,</span>
        </li>
        <li class="service">
          <div class="service-photo walking" role="img" aria-label="Photo of a dog on a lead walking in a park"></div>
          <span class="service-caption">Dog Walking</span>
        </li>
      </ul>
      <div class="services-heading">
        <span>OUR</span>
        <span>THREE</span>
        <span>SERVICES</span>
      </div>
    </aside>
  </article>
</main>
</body>
</html>
```